Flyer Lieferservice / Gutschein / Visitenkarte
Zielgruppe
Restaurant
Aufgabenstellung
Wir benötigen:
Lieferservice Flyer mit Speisekarte
Gutschein Flyer
Visitenkarten
Farbe: Schwarz & Gold siehe Website
Speisekarte: (siehe Anhang)
Wichtige Inhalte:
Speiskarte
Social Media
Anschrift
Telefonnummer
Website
App Verweis
(bishergie Flyer zur Ansicht im Anhang)

```html
<!DOCTYPE html>
<html lang="de">
<head>
<meta charset="utf-8">
<title>Lieferservice Flyer – Brasserie Nordlicht</title>
<link href="https://fonts.googleapis.com/css2?family=Montserrat:wght@300;400;500;600&family=Allura&display=swap" rel="stylesheet">
<style>
  :root{
    --bg:#d6d5d1;
    --black:#141312;
    --black-soft:#1d1c1a;
    --gold:#d9a92a;
    --gold-line:#c99a22;
    --white:#f2f1ee;
    --text-light:#e6e4df;
    --ink:#2a2926;
  }
  *{box-sizing:border-box;margin:0;padding:0}
  html,body{width:1200px;height:960px;overflow:hidden;background:var(--bg)}
  body{font-family:"Montserrat",sans-serif;display:flex;gap:26px;align-items:center;justify-content:center}

  .page{width:566px;height:800px;position:relative;overflow:hidden;box-shadow:0 10px 30px rgba(0,0,0,.25)}

  /* ---------- Menu page ---------- */
  .menu{background:var(--black);color:var(--text-light);padding:34px 34px 30px;font-weight:300;font-size:9.6px;line-height:13.6px}
  .section-head{border-top:1px solid var(--gold-line);border-bottom:1px solid var(--gold-line);padding:7px 0;margin:0 0 10px}
  .section-head h2{color:var(--gold);font-weight:400;font-size:19px;letter-spacing:3px;text-align:center}
  .items{list-style:none}
  .items li{display:flex;justify-content:space-between;gap:10px}
  .items .price{white-space:nowrap}
  .extras{display:flex;justify-content:space-between;margin:8px 0 22px;font-size:9.4px}
  .extras b{font-weight:600}
  .two-col{display:grid;grid-template-columns:1fr 1fr;gap:26px;margin-bottom:22px}
  .note{margin-bottom:2px}
  .salad-note{margin-top:8px}

  /* ---------- Cover page ---------- */
  .cover{background:var(--black)}
  .cover .frame{position:absolute;left:14px;top:14px;right:14px;height:560px;border:2px solid var(--white);overflow:hidden;background:var(--black-soft)}
  .photo{position:absolute;left:120px;top:200px;width:430px;height:360px;background:radial-gradient(ellipse at 60% 55%,#6b4a22 0%,#3a2a16 38%,#1d1a16 70%,#1d1c1a 100%)}
  .brand{position:absolute;left:30px;top:44px;color:var(--gold);font-size:28px;font-weight:400;letter-spacing:.5px}
  .web{position:absolute;left:30px;top:90px;color:var(--text-light);font-size:12px;font-weight:300;letter-spacing:.4px}
  .order{position:absolute;left:0;bottom:40px;display:flex;align-items:center}
  .order .label{background:#0c0b0b;color:var(--white);font-size:17px;letter-spacing:3px;padding:14px 22px 14px 28px;font-weight:400}
  .order .phone{background:var(--gold);color:var(--white);font-size:20px;font-weight:500;letter-spacing:3px;padding:12px 30px;border-radius:0 26px 26px 0}

  .panel{position:absolute;left:14px;right:14px;bottom:14px;top:560px;background:var(--white);padding:26px 30px 0;text-align:center}
  .app-title{font-family:"Allura",cursive;font-size:42px;font-weight:400;color:var(--ink);line-height:44px}
  .badges{display:flex;justify-content:center;gap:18px;margin:12px 0 14px}
  .badge{width:120px;height:36px;background:#111;border-radius:6px}
  .rule{width:300px;height:1px;background:#555;margin:0 auto 12px}
  .info{color:var(--gold);font-size:9.4px;line-height:14px;font-weight:400}
  .info b{font-weight:600}
</style>
</head>
<body>

<article class="page menu">
  <section>
    <div class="section-head"><h2>FLEISCH</h2></div>
    <ul class="items">
      <li><span>Schnitzel „Wiener Art“ mit Beilagen &amp; Soße nach Wahl</span><span class="price">klein 7,90 EUR | groß 11,90 EUR</span></li>
      <li><span>Putenschnitzel mit Beilagen &amp; Soße nach Wahl</span><span class="price">klein 9,90 EUR | groß 13,90 EUR</span></li>
      <li><span>Wiener Schnitzel vom Kalb mit Beilagen &amp; Soße nach Wahl</span><span class="price">18,90 EUR</span></li>
      <li><span>Cordon Bleu mit Beilagen &amp; Soße nach Wahl</span><span class="price">14,90 EUR</span></li>
      <li><span>Sonne Cordon Bleu | Gefüllt mit Tomate-Mozzarella und frischem Basilikum &amp; Beilage/Soße</span><span class="price">16,90 EUR</span></li>
      <li><span>Weiden Cordon Bleu | Gefüllt mit Ziegenfrischkäse, Schinken und Honig &amp; Beilage/Soße</span><span class="price">16,90 EUR</span></li>
      <li><span>Mediterranes Cordon Bleu | gefüllt mit Schafskäse, Oliven und Pepperonis &amp; Beilage/Soße</span><span class="price">16,90 EUR</span></li>
      <li><span>Krustenschnitzel | Schweineschnitzel mit Goudakäse und Jägersoße überbacken &amp; Beilage</span><span class="price">13,90 EUR</span></li>
      <li><span>Schnitzel Bolognese mit Beilage nach Wahl</span><span class="price">14,90 EUR</span></li>
      <li><span>Schnitzel Hawaii mit Beilage nach Wahl</span><span class="price">14,90 EUR</span></li>
      <li><span>Rinderbraten mit Beilagen &amp; Soße nach Wahl</span><span class="price">15,90 EUR</span></li>
      <li><span>Wildragout mit Beilagen nach Wahl</span><span class="price">16,90 EUR</span></li>
      <li><span>Zartes Rindergulasch mit Spätzle</span><span class="price">16,90 EUR</span></li>
      <li><span>Puten-Nuggets mit Pommes</span><span class="price">klein 5,90 EUR | groß 8,90 EUR</span></li>
      <li><span>Spaghetti Bolognese</span><span class="price">klein 7,80 EUR | groß 9,90 EUR</span></li>
    </ul>
    <div class="extras">
      <span><b>BEILAGEN</b> Pommes | Kroketten | Spätzle</span>
      <span><b>SOSSEN</b> Bratensoße | Jägersoße | Pikante Paprikasoße</span>
    </div>
  </section>

  <div class="two-col">
    <section>
      <div class="section-head"><h2>VEGETARISCH</h2></div>
      <ul class="items">
        <li><span>Kräuterpfannkuchen gefüllt mit Champignons</span><span class="price">10,90 EUR</span></li>
        <li><span>Käsespätzle</span><span class="price">klein 7,90 | groß 10,90 EUR</span></li>
        <li><span>Selbstgemachte Serviettenknödel mit Jägersoße</span><span class="price">7,90 EUR</span></li>
        <li><span>Gegrillter Schafskäse | Knoblauch, Zwiebeln, Oliven, Paprika, Tomaten, Peperoni</span><span class="price">7,90 EUR</span></li>
      </ul>
    </section>
    <section>
      <div class="section-head"><h2>FISCH</h2></div>
      <ul class="items">
        <li><span>Kräuterlachs aus dem Ofen mit Kartoffelsalat</span><span class="price">17,90 EUR</span></li>
        <li><span>Paniertes Zanderfilet mit Kartoffelsalat</span><span class="price">15,90 EUR</span></li>
      </ul>
    </section>
  </div>

  <section>
    <div class="section-head"><h2>SALAT</h2></div>
    <p class="note">Alle Salate werden serviert mit Krautsalat, Karottensalat, Rotkohlsalat, grüner Salat, Tomate &amp; Gurke</p>
    <ul class="items">
      <li><span>Beilagensalat</span><span class="price">4,50 EUR</span></li>
      <li><span>Kartoffelsalat</span><span class="price">4,50 EUR</span></li>
      <li><span>Gemischter Salat</span><span class="price">7,90 EUR</span></li>
      <li><span>Fitnesssalat mit Putenstreifen</span><span class="price">11,90 EUR</span></li>
      <li><span>Salat mit Gemüsemaultaschen</span><span class="price">11,90 EUR</span></li>
      <li><span>Salat Schafskäse mit Oliven und Pepperonis</span><span class="price">10,90 EUR</span></li>
      <li><span>Salat mit Schinken/Käse und Zwiebeln</span><span class="price">9,80 EUR</span></li>
    </ul>
    <p class="salad-note">Als Dressing stehen wahlweise unser Hausdressing oder Balsamico Honig-Senf Dressing zur Verfügung</p>
  </section>
</article>

<article class="page cover">
  <div class="frame">
    <div class="photo" role="img" aria-label="Foto: gebackene Kartoffeln mit Kräutern in einer dunklen Pfanne"></div>
    <p class="brand">Brasserie Nordlicht</p>
    <p class="web">brasserie-nordlicht.de</p>
    <div class="order">
      <span class="label">BESTELLE UNTER</span>
      <span class="phone">030418 | 5520731</span>
    </div>
  </div>
  <div class="panel">
    <h2 class="app-title">Liefershop – jetzt auch als App</h2>
    <div class="badges">
      <span class="badge"></span>
      <span class="badge"></span>
    </div>
    <div class="rule"></div>
    <p class="info"><b>Öffnungszeiten:</b> Mittwoch - Samstag von 17 Uhr bis 21:30 | Sonn- und Feiertag von 11 Uhr bis 21:30 Uhr</p>
    <p class="info"><b>Liefergebiete:</b> Lindenau-Hochfeld | Dettenau | Eggenbach-Leopoldsau | Graben-Neuried |<br>Stutenried | Karlshof-Neuhard | Neurath bzw. PLZ 70149</p>
  </div>
</article>

</body>
</html>
```